Alternative Health business needs a self help book cover design

Pale Brook Healing requires an E book and print cover design for a new self help book titled "Making The Bright Choice". Sub title 'Ways to build the glad days YOU seek' . Author Dorinda Crastley. The book is about deliberately changing things now, so you feel happy now and this then flows out an effects everything else in your life. It combines NLP, yoga philosophy and modern psychology in a down to earth, easy to read manner. I would like the cover to be happy, colourful, beautiful, artistic and hip. Maybe something hand drawn or painted. Something a woman would want to display and something that makes you smile and feel happy.
I don't want it to look like a romance novel and would prefer no photos of people. Pics are of other peoples covers I like. Thank you in advance. dorinda

Target Market(s)

woman 18-50

Industry/Entity Type

Business

Requirements
Must have
• happy feeling. professional look
Nice to have
• original drawing or painting
Should not have
• photos of real people, yellow smiley faces, sunsets, butterflies, yoga, tree, elements of my business logo

```html
<!DOCTYPE html>
<html lang="en">
<head>
<meta charset="utf-8">
<title>Making The Bright Choice – Book Cover</title>
<link rel="stylesheet" href="https://fonts.googleapis.com/css2?family=Bodoni+Moda:opsz,wght@6..96,400&display=swap">
<style>
  :root {
    --backdrop: #bfbebf;
    --band-orange: #ff9400;
    --emblem-tone: #d97a00;
    --panel-white: #fbfcfb;
    --ink: #0a0a0a;
  }
  html, body {
    margin: 0;
    padding: 0;
    width: 1200px;
    height: 900px;
    overflow: hidden;
    background: var(--backdrop);
  }
  .cover {
    position: absolute;
    left: 326px;
    top: 0;
    width: 636px;
    height: 900px;
    display: flex;
  }
  .cover-band {
    position: relative;
    width: 272px;
    height: 100%;
    background: var(--band-orange);
  }
  .cover-emblem {
    position: absolute;
    left: 81px;
    top: 99px;
    width: 172px;
    height: 172px;
    border-radius: 50%;
    background: var(--emblem-tone);
  }
  .cover-panel {
    position: relative;
    width: 364px;
    height: 100%;
    background: var(--panel-white);
    font-family: "Bodoni Moda", "Didot", serif;
    color: var(--ink);
  }
  .book-title {
    position: absolute;
    right: 50px;
    top: 104px;
    margin: 0;
    font-weight: 400;
    font-size: 96px;
    line-height: 92px;
    letter-spacing: -3px;
    text-align: right;
    white-space: nowrap;
  }
  .book-title span { display: block; }
  .book-subtitle {
    position: absolute;
    right: 54px;
    top: 600px;
    margin: 0;
    font-size: 24px;
    line-height: 27px;
    text-align: right;
    letter-spacing: -0.3px;
  }
  .book-subtitle span { display: block; }
  .book-author {
    position: absolute;
    right: 52px;
    top: 794px;
    margin: 0;
    font-size: 42px;
    font-weight: 400;
    letter-spacing: -0.8px;
    white-space: nowrap;
  }
</style>
</head>
<body>
  <main class="cover">
    <div class="cover-band">
      <div class="cover-emblem" role="img" aria-label="Simple smiling emblem drawn in black line"></div>
    </div>
    <section class="cover-panel">
      <h1 class="book-title">
        <span>Making</span>
        <span>The</span>
        <span>Bright</span>
        <span>Choice</span>
      </h1>
      <p class="book-subtitle">
        <span>Ways to build the</span>
        <span>glad days</span>
        <span>YOU seek</span>
      </p>
      <p class="book-author">Dorinda Crastley</p>
    </section>
  </main>
</body>
</html>
```